Kobalto Cell Phone Repair

We are a small cell phone repair store in need of a redesign to our current business card to make it a more modern, cleaner design that will catch folks' attention (perhaps with rounded edges ) - But still include most of the information listed on the current card. Would like to keep the current color scheme of black/white and green. Card will not need any personnel name included. Would like to see some designs include takes on a velorin or tekvo screen as well as more traditional cards.

Target Market(s)

broad spectrum across all cell phone users

Industry/Entity Type

Cell Phone

Contact Information for Business Card

changes to front text:
keep business Logo
business address, phone number website and email. All other info optional (add gathernest and blurvo icons on card

Rear of card:

Keep repair services, change tekvo repair to slatra repair, change quorvex os repair to data recovery (with appropriate icon or substitute)
remove products text
remove pjw and ravesh from manufacturer logos, add dunbelio.

Requirements
Must have
• business Logo
• business address, phone number website and email
• keep colors to white/black/green/gray
• gathernest and blurvo icons on card
Nice to have
• Would like to see 'traditional' business card design as well as creative design incorporating incorporating front of cell phone (eg tekvo or quorvex). Rounded edges would be nice but not necessary.

```html
<!DOCTYPE html>
<html lang="en">
<head>
<meta charset="utf-8">
<title>Kobalto Cell Phone Repair – Business Card</title>
<link rel="stylesheet" href="https://fonts.googleapis.com/css2?family=Arimo:wght@400;700&display=swap">
<style>
  :root {
    --stage: #555555;
    --black: #000000;
    --white: #ffffff;
    --green: #5fac45;
    --green-text: #4fa63a;
    --green-dark: #2f7d2a;
    --gray: #9a9a9a;
    --gray-dark: #444444;
    --rule: #8a8a8a;
  }
  * { margin: 0; padding: 0; box-sizing: border-box; }
  html, body { width: 1200px; height: 900px; overflow: hidden; background: var(--stage); }
  body { position: relative; font-family: "Arimo", Arial, sans-serif; }

  .card {
    position: absolute; top: 171px; width: 348px; height: 561px;
    border-radius: 22px; overflow: hidden;
    box-shadow: 2px 3px 4px rgba(0,0,0,0.45);
  }
  .card-front { left: 259px; background: var(--white); }
  .card-back { left: 631px; background: var(--green); }

  /* front: phone frame */
  .frame-top, .frame-bottom { position: absolute; left: 0; width: 100%; background: var(--black); }
  .frame-top { top: 0; height: 67px; }
  .frame-bottom { bottom: 0; height: 74px; }
  .speaker-dot { position: absolute; left: 166px; top: 20px; width: 15px; height: 15px; border-radius: 50%; background: var(--gray); }
  .speaker-bar { position: absolute; left: 145px; top: 42px; width: 58px; height: 4px; border-radius: 2px; background: var(--gray); }
  .home-button { position: absolute; left: 151px; top: 14px; width: 46px; height: 46px; border-radius: 50%; background: var(--gray-dark); }
  .home-button::after { content: ""; position: absolute; left: 17px; top: 17px; width: 12px; height: 12px; border-radius: 50%; background: var(--black); }

  .brand { position: absolute; left: 40px; top: 104px; width: 270px; height: 142px; }
  .brand-mark { position: absolute; left: 0; top: 22px; width: 70px; height: 70px; border-radius: 50%; background: var(--green); }
  .brand-name {
    position: absolute; left: 80px; top: 12px; width: 190px;
    color: var(--black); font-weight: 700; text-align: right; line-height: 1;
  }
  .brand-name .word { display: block; font-size: 46px; letter-spacing: -1px; }
  .brand-name .tag { display: block; font-size: 17px; margin-top: 10px; }

  .contact { position: absolute; left: 0; top: 274px; width: 100%; text-align: center; font-size: 15px; line-height: 20px; color: var(--black); }
  .contact .label { color: var(--green-text); font-weight: 700; }
  .contact .web { color: var(--green-text); font-weight: 700; }
  .rule { position: absolute; left: 79px; width: 190px; height: 1px; background: var(--rule); }
  .rule-1 { top: 341px; }
  .rule-2 { top: 386px; }
  .address { position: absolute; left: 0; top: 353px; width: 100%; text-align: center; font-size: 16px; color: var(--black); }
  .services-list { position: absolute; left: 0; top: 397px; width: 100%; text-align: center; font-size: 15px; line-height: 20px; color: var(--black); list-style: none; }

  /* back */
  .target { position: absolute; left: 30px; top: 22px; width: 32px; height: 32px; border-radius: 50%; border: 4px solid var(--green-dark); }
  .target::after { content: ""; position: absolute; left: 6px; top: 6px; width: 12px; height: 12px; border-radius: 50%; background: var(--green-dark); }

  .repair-list { position: absolute; left: 64px; top: 93px; list-style: none; }
  .repair-item { display: flex; align-items: center; height: 52px; }
  .repair-icon { width: 43px; height: 43px; border-radius: 5px; border: 2px solid var(--white); flex: none; }
  .repair-label { margin-left: 4px; color: var(--white); font-weight: 700; font-size: 15px; letter-spacing: 0.2px; }

  .back-rule { position: absolute; left: 61px; top: 418px; width: 230px; height: 1px; background: rgba(255,255,255,0.45); }

  .makers { position: absolute; left: 0; top: 0; width: 100%; height: 100%; list-style: none; }
  .maker { position: absolute; color: var(--white); font-weight: 700; display: flex; align-items: center; gap: 5px; }
  .maker .dot { width: 18px; height: 18px; border-radius: 50%; background: var(--white); }
  .m1 { left: 38px; top: 454px; font-size: 20px; }
  .m2 { left: 195px; top: 450px; font-size: 24px; }
  .m3 { left: 34px; top: 498px; font-size: 25px; }
  .m4 { left: 152px; top: 502px; font-size: 20px; }
  .m5 { left: 262px; top: 508px; font-size: 14px; }
</style>
</head>
<body>

<section class="card card-front" aria-label="Business card front">
  <div class="frame-top">
    <span class="speaker-dot"></span>
    <span class="speaker-bar"></span>
  </div>

  <div class="brand">
    <span class="brand-mark"></span>
    <h1 class="brand-name"><span class="word">KOBALTO</span><span class="tag">CELL PHONE REPAIR</span></h1>
  </div>

  <div class="contact">
    <p><span class="label">P:</span> 555.014.2276</p>
    <p><span class="label">E:</span> info@kobaltorepair.com</p>
    <p class="web">www.kobaltorepair.com</p>
  </div>
  <div class="rule rule-1"></div>
  <p class="address">2417 Fennick Ave, Marlow MD 21209</p>
  <div class="rule rule-2"></div>
  <ul class="services-list">
    <li>Unlocking &amp; Flashing Services</li>
    <li>Smart Phones &amp; Accessories</li>
    <li>Water Damage Repair | Screen Repair</li>
  </ul>

  <div class="frame-bottom"><span class="home-button"></span></div>
</section>

<section class="card card-back" aria-label="Business card back">
  <span class="target"></span>

  <ul class="repair-list">
    <li class="repair-item"><span class="repair-icon" role="img" aria-label="Phone with cracked screen" style="background:linear-gradient(#f2f2f2,#2a2a2a)"></span><span class="repair-label">CRACKED SCREEN</span></li>
    <li class="repair-item"><span class="repair-icon" role="img" aria-label="Phone splashing in water" style="background:linear-gradient(#d8e6ef,#3f7fa8)"></span><span class="repair-label">WATER DAMAGE</span></li>
    <li class="repair-item"><span class="repair-icon" role="img" aria-label="Close-up of a charging port" style="background:linear-gradient(#c9c9c9,#3a3a3a)"></span><span class="repair-label">CHARGING PORT</span></li>
    <li class="repair-item"><span class="repair-icon" role="img" aria-label="Phone with colourful app icons" style="background:linear-gradient(135deg,#f0f0f0,#3a6fb0)"></span><span class="repair-label">DATA RECOVERY</span></li>
    <li class="repair-item"><span class="repair-icon" role="img" aria-label="Phone screen with unlocked padlock" style="background:linear-gradient(#5a3a2a,#1a1a1a)"></span><span class="repair-label">CELLPHONE UNLOCK</span></li>
    <li class="repair-item"><span class="repair-icon" role="img" aria-label="Tablets stacked together" style="background:linear-gradient(#f4f4f4,#555)"></span><span class="repair-label">SLATRA REPAIR</span></li>
  </ul>

  <div class="back-rule"></div>

  <ul class="makers" aria-label="Brands serviced">
    <li class="maker m1">Brambury</li>
    <li class="maker m2"><span class="dot"></span>Kelto</li>
    <li class="maker m3">tekvo</li>
    <li class="maker m4">VELORIN</li>
    <li class="maker m5">DUNBELIO</li>
  </ul>
</section>

</body>
</html>
```